Driver License Monitoring Application Marketing Website

We need a new web design for our web application. The product is called "PermitSentry." We provide a driver license monitoring service to companies and local government bodies with driver fleets. Our current website is available at www.PermitSentry-demo.net.

I prefer a clean, single-page design with good SEO. Attached are some PDFs with data about the project.

Target Market(s)

Companies with driver fleets, local government.

Industry/Entity Type

Government

Coding

Coded - Design and coding required

Number of Pages Required

1 page

Colors
000000

Requirements
Must have
• Content from current www.PermitSentry-demo.net and attached PDFs.
Nice to have
• Prefer a simple Bootstrap or similar design for easy editing.
• Room for a simple video explanation of how the product works (we don't have an actual video yet)

```html
<!DOCTYPE html>
<html lang="en">
<head>
<meta charset="utf-8">
<title>PermitSentry – Driver License Monitoring</title>
<link rel="stylesheet" href="https://fonts.googleapis.com/css2?family=Cinzel:wght@400;700&family=Open+Sans:wght@300;400;600;700&display=swap">
<style>
:root{
  --red:#c1121f;
  --red-dark:#8e0c16;
  --ink:#141414;
  --panel:#1c1c1c;
  --panel-2:#232323;
  --line:#333;
  --muted:#9a9a9a;
  --paper:#ffffff;
  --text:#444;
}
*{box-sizing:border-box;margin:0;padding:0}
html,body{width:1200px;height:3272px;overflow:hidden}
body{font-family:"Open Sans",Arial,sans-serif;color:var(--text);background:var(--paper);position:relative}
.serif{font-family:"Cinzel",Georgia,serif}
.btn{display:inline-flex;align-items:center;justify-content:center;height:44px;padding:0 36px;font-size:11px;font-weight:600;letter-spacing:1px;text-transform:uppercase;color:#fff;background:var(--red);border:0}
.btn-ghost{background:rgba(0,0,0,.55);border:1px solid rgba(255,255,255,.25)}
.eyebrow{font-family:"Cinzel",Georgia,serif;color:var(--red);font-size:22px;font-weight:700;text-align:center}
.section-title{font-size:32px;font-weight:300;text-align:center}

/* Header */
.site-header{position:absolute;top:0;left:0;width:1200px;height:72px;background:var(--ink);display:flex;align-items:center;padding:0 172px}
.brand{font-family:"Cinzel",Georgia,serif;font-weight:700;font-size:18px;color:#fff;letter-spacing:1px}
.main-nav{margin-left:auto;display:flex;align-items:center;height:72px}
.main-nav a{color:#ddd;font-size:11px;padding:0 18px;height:72px;display:flex;align-items:center;text-decoration:none}
.main-nav a.active{background:var(--red);color:#fff}
.nav-search{margin:0 16px}
.btn-login{height:30px;padding:0 30px;border-radius:15px;font-size:10px}

/* Hero */
.hero{position:absolute;top:72px;left:0;width:1200px;height:520px;text-align:center;color:#fff}
.hero-photo{position:absolute;inset:0;background:radial-gradient(ellipse at 50% 80%,rgba(210,120,40,.55),transparent 60%),linear-gradient(180deg,#1a1410 0%,#3a2216 45%,#6a3a18 70%,#1d1410 100%)}
.hero-shade{position:absolute;inset:0;background:rgba(0,0,0,.35)}
.hero-content{position:relative;padding-top:76px}
.hero-title{font-family:"Cinzel",Georgia,serif;font-weight:700;font-size:64px;letter-spacing:6px;line-height:1}
.hero-sub{font-family:"Cinzel",Georgia,serif;font-size:40px;letter-spacing:3px;margin-top:14px;line-height:1}
.hero-text{width:600px;margin:40px auto 0;font-size:17px;line-height:26px;color:#eee}
.hero-actions{margin-top:76px;display:flex;gap:32px;justify-content:center}
.hero-actions .btn{width:190px;padding:0}
.slider-arrow{position:absolute;top:304px;width:40px;height:40px;border-radius:50%;background:rgba(255,255,255,.15);display:flex;align-items:center;justify-content:center}
.slider-arrow.prev{left:68px}.slider-arrow.next{right:68px}

/* Welcome */
.welcome{position:absolute;top:592px;left:0;width:1200px;height:336px;background:var(--paper)}
.video-frame{position:absolute;left:172px;top:60px;width:400px;height:216px;background:linear-gradient(135deg,#5a5f66,#1e2125 60%,#3a3d42);display:flex;align-items:center;justify-content:center}
.welcome-body{position:absolute;left:612px;top:76px;width:416px}
.welcome-title{font-family:"Cinzel",Georgia,serif;font-size:24px;font-weight:700;color:#222}
.welcome-title em{font-style:normal;color:var(--red)}
.welcome-kicker{font-size:13px;color:#666;margin-top:6px}
.welcome-text{font-size:12px;line-height:19px;color:#777;margin-top:14px}
.welcome-body .btn{margin-top:20px;height:38px;padding:0 28px;font-size:10px}

/* Services */
.services{position:absolute;top:928px;left:0;width:1200px;height:1152px;background:var(--ink);color:#ddd}
.services .eyebrow{position:absolute;top:72px;width:1200px}
.services .section-title{position:absolute;top:118px;width:1200px;color:#fff}
.service-tabs{position:absolute;top:232px;left:172px;width:856px;height:112px;display:grid;grid-template-columns:repeat(4,1fr);border:1px solid var(--line)}
.service-tab{display:flex;flex-direction:column;align-items:center;justify-content:center;border-right:1px solid var(--line);color:var(--muted)}
.service-tab:last-child{border-right:0}
.service-tab .tab-label{font-family:"Cinzel",Georgia,serif;font-size:15px;margin-top:10px;color:#ccc}
.service-tab .tab-note{font-size:10px;margin-top:4px}
.service-tab.active{border-bottom:3px solid var(--red)}
.service-tab.active .tab-label{color:#fff}
.fleet-photo{position:absolute;top:412px;left:172px;width:428px;height:260px;background:linear-gradient(180deg,#6fa8dc 0%,#b9d6ee 50%,#3d4b5a 80%,#2a2f36 100%)}
.fleet-body{position:absolute;top:424px;left:624px;width:404px}
.fleet-title{font-family:"Cinzel",Georgia,serif;color:var(--red);font-size:22px;font-weight:700;line-height:28px;text-transform:uppercase}
.fleet-lead{color:#fff;font-size:14px;font-weight:600;margin-top:14px}
.fleet-text{font-size:12px;line-height:19px;color:#999;margin-top:10px}
.fleet-body .btn{margin-top:18px;height:36px;padding:0 26px;font-size:10px}
.sectors{position:absolute;top:724px;left:172px;width:856px;display:grid;grid-template-columns:repeat(4,199px);gap:20px}
.sector-photo{height:216px}
.sector-label{text-align:center;font-size:11px;color:var(--muted);margin-top:16px;letter-spacing:.5px;text-transform:uppercase}
.services .more{position:absolute;top:1048px;left:505px;width:190px}

/* Benefits */
.benefits{position:absolute;top:2080px;left:0;width:1200px;height:620px;background:var(--paper)}
.benefits .eyebrow{position:absolute;top:56px;width:1200px}
.benefits .section-title{position:absolute;top:102px;width:1200px;color:#333}
.benefit-grid{position:absolute;top:188px;left:172px;width:856px;height:280px;background:var(--panel);display:grid;grid-template-columns:repeat(3,1fr);grid-template-rows:repeat(2,1fr)}
.benefit{display:flex;flex-direction:column;align-items:center;justify-content:center;border-right:1px solid var(--line);border-bottom:1px solid var(--line);color:#bbb}
.benefit:nth-child(3n){border-right:0}
.benefit:nth-child(n+4){border-bottom:0}
.benefit span{font-size:11px;margin-top:14px;text-transform:uppercase;letter-spacing:.5px}
.benefits .more{position:absolute;top:536px;left:524px;width:152px}

/* Footer */
.site-footer{position:absolute;top:2700px;left:0;width:1200px;height:460px;background:linear-gradient(180deg,#1b1b1b,#121212);text-align:center;color:#aaa}
.footer-pin{position:absolute;top:72px;left:582px}
.footer-brand{position:absolute;top:150px;width:1200px;font-family:"Cinzel",Georgia,serif;font-weight:700;font-size:24px;color:#fff;letter-spacing:2px}
.footer-note{position:absolute;top:194px;width:1200px;font-size:11px;color:#888}
.contact-row{position:absolute;top:272px;left:216px;width:768px;display:grid;grid-template-columns:repeat(3,1fr);gap:40px}
.contact-card{height:116px;border:1px solid var(--line);background:rgba(255,255,255,.03);display:flex;flex-direction:column;align-items:center;justify-content:center;gap:14px;color:#fff;font-size:14px;font-weight:600;letter-spacing:.5px}
.bottom-bar{position:absolute;top:3160px;left:0;width:1200px;height:112px;background:var(--red-dark);display:flex;align-items:center;padding:0 172px;color:#f1d5d7;font-size:10px;letter-spacing:.5px}
.social{margin-left:auto;display:flex;gap:14px}
.social i{display:block;width:30px;height:30px;background:rgba(0,0,0,.25)}
</style>
</head>
<body>

<header class="site-header">
  <div class="brand">PermitSentry</div>
  <nav class="main-nav">
    <a class="active" href="#">Home</a>
    <a href="#">About Us</a>
    <a href="#">License Monitoring</a>
    <a href="#">Contact</a>
    <svg class="nav-search" width="14" height="14" viewBox="0 0 14 14"><circle cx="6" cy="6" r="4.5" fill="none" stroke="#ccc" stroke-width="1.5"/><line x1="9.5" y1="9.5" x2="13" y2="13" stroke="#ccc" stroke-width="1.5"/></svg>
    <span class="btn btn-login">Login</span>
  </nav>
</header>

<section class="hero">
  <div class="hero-photo" role="img" aria-label="Night city street with glowing light trails of moving traffic"></div>
  <div class="hero-shade"></div>
  <div class="hero-content">
    <h1 class="hero-title">Florida</h1>
    <p class="hero-sub">Driver License Monitoring</p>
    <p class="hero-text">Monitor your fleet <b>electronically</b>. Get alerts by <b>email</b> and <b>online</b>. Never let another unlicensed or unauthorized driver behind the wheel.</p>
    <div class="hero-actions">
      <span class="btn btn-ghost">Read More</span>
      <span class="btn">Track Your Fleet</span>
    </div>
  </div>
  <span class="slider-arrow prev"><svg width="12" height="12" viewBox="0 0 12 12"><path d="M8 1 3 6l5 5" fill="none" stroke="#fff" stroke-width="1.8"/></svg></span>
  <span class="slider-arrow next"><svg width="12" height="12" viewBox="0 0 12 12"><path d="M4 1l5 5-5 5" fill="none" stroke="#fff" stroke-width="1.8"/></svg></span>
</section>

<section class="welcome">
  <div class="video-frame" role="img" aria-label="Video placeholder showing a dark sports car on a road">
    <svg width="64" height="64" viewBox="0 0 64 64"><circle cx="32" cy="32" r="30" fill="rgba(0,0,0,.35)" stroke="#fff" stroke-width="2"/><path d="M26 20v24l19-12z" fill="#fff"/></svg>
  </div>
  <div class="welcome-body">
    <h2 class="welcome-title">Welcome To <em>PermitSentry</em></h2>
    <p class="welcome-kicker">Watch A Video Now!</p>
    <p class="welcome-text">We help companies and local government bodies keep every driver on the road properly licensed. Our service checks driver records automatically and tells you the moment a license is suspended, expired or revoked, so your fleet stays safe and compliant without the paperwork.</p>
    <span class="btn">Read More</span>
  </div>
</section>

<section class="services">
  <p class="eyebrow">Our Services</p>
  <h2 class="section-title">Driver License Monitoring Services</h2>

  <div class="service-tabs">
    <div class="service-tab active">
      <svg width="26" height="20" viewBox="0 0 26 20"><rect x="1" y="1" width="24" height="18" fill="none" stroke="#888" stroke-width="1.5"/><line x1="5" y1="7" x2="21" y2="7" stroke="#888"/><line x1="5" y1="12" x2="17" y2="12" stroke="#888"/></svg>
      <span class="tab-label">What We Do</span><span class="tab-note">license monitoring</span>
    </div>
    <div class="service-tab">
      <svg width="28" height="20" viewBox="0 0 28 20"><rect x="1" y="4" width="17" height="11" fill="none" stroke="#888" stroke-width="1.5"/><path d="M18 8h5l4 4v3h-9z" fill="none" stroke="#888" stroke-width="1.5"/><circle cx="7" cy="17" r="2" fill="#888"/><circle cx="22" cy="17" r="2" fill="#888"/></svg>
      <span class="tab-label">Commercial</span><span class="tab-note">private sector</span>
    </div>
    <div class="service-tab">
      <svg width="26" height="22" viewBox="0 0 26 22"><path d="M1 8 13 1l12 7z" fill="none" stroke="#888" stroke-width="1.5"/><path d="M4 10v8M10 10v8M16 10v8M22 10v8M1 21h24" stroke="#888" stroke-width="1.5"/></svg>
      <span class="tab-label">Government</span><span class="tab-note">public sector</span>
    </div>
    <div class="service-tab">
      <svg width="22" height="22" viewBox="0 0 22 22"><path d="M11 1l3 7 7 .6-5.3 4.6 1.7 7.3L11 16.6 4.6 20.5l1.7-7.3L1 8.6 8 8z" fill="none" stroke="#888" stroke-width="1.5"/></svg>
      <span class="tab-label">About Us</span><span class="tab-note">our story and team</span>
    </div>
  </div>

  <div class="fleet-photo" role="img" aria-label="Blue semi truck with white trailer on the highway"></div>
  <div class="fleet-body">
    <h3 class="fleet-title">Track your fleet for<br>safety &amp; performance</h3>
    <p class="fleet-lead">Monitor your drivers electronically, twenty-four hours a day.</p>
    <p class="fleet-text">Every driver in your fleet is checked against state records on a set schedule. When a status changes you receive an alert by email and see it in your online dashboard, with clear steps to follow. Keep risk low, protect your company and stay ahead of insurance and audit requirements.</p>
    <span class="btn">Read More</span>
  </div>

  <div class="sectors">
    <div>
      <div class="sector-photo" role="img" aria-label="Red delivery truck at sunset" style="background:linear-gradient(180deg,#f0a04a,#b0452a 60%,#3a1a12)"></div>
      <p class="sector-label">Commercial Sector</p>
    </div>
    <div>
      <div class="sector-photo" role="img" aria-label="Row of yellow school buses" style="background:linear-gradient(180deg,#7da7d4,#e2b229 55%,#4a3d20)"></div>
      <p class="sector-label">School Districts</p>
    </div>
    <div>
      <div class="sector-photo" role="img" aria-label="City street at night with taxis" style="background:linear-gradient(180deg,#2a2030,#b8862a 55%,#5a2a1a)"></div>
      <p class="sector-label">Government</p>
    </div>
    <div>
      <div class="sector-photo" role="img" aria-label="Small red car on a green lawn" style="background:linear-gradient(180deg,#a8c8e8,#5a9a3a 55%,#2e5a22)"></div>
      <p class="sector-label">Insurance Agents</p>
    </div>
  </div>
  <span class="btn more">Read More</span>
</section>

<section class="benefits">
  <p class="eyebrow">Our Benefits</p>
  <h2 class="section-title">Driver License Monitoring Services</h2>
  <div class="benefit-grid">
    <div class="benefit"><svg width="28" height="24" viewBox="0 0 28 24"><rect x="1" y="1" width="26" height="17" fill="none" stroke="#aaa" stroke-width="1.5"/><path d="M9 23h10M14 18v5" stroke="#aaa" stroke-width="1.5"/></svg><span>License Monitoring</span></div>
    <div class="benefit"><svg width="20" height="26" viewBox="0 0 20 26"><rect x="6" y="1" width="8" height="14" rx="4" fill="none" stroke="#aaa" stroke-width="1.5"/><path d="M2 11a8 8 0 0 0 16 0M10 19v6" fill="none" stroke="#aaa" stroke-width="1.5"/></svg><span>Alerts by Email</span></div>
    <div class="benefit"><svg width="26" height="24" viewBox="0 0 26 24"><path d="M13 2 24 22H2z" fill="none" stroke="#aaa" stroke-width="1.5"/><path d="M13 9v6M13 18v1" stroke="#aaa" stroke-width="1.5"/></svg><span>Reduce Insurance Cost</span></div>
    <div class="benefit"><svg width="24" height="24" viewBox="0 0 24 24"><circle cx="12" cy="12" r="10.5" fill="none" stroke="#aaa" stroke-width="1.5"/><path d="M12 6v6l4 3" fill="none" stroke="#aaa" stroke-width="1.5"/></svg><span>Real Time Vigilance</span></div>
    <div class="benefit"><svg width="26" height="24" viewBox="0 0 26 24"><circle cx="9" cy="8" r="4" fill="none" stroke="#aaa" stroke-width="1.5"/><circle cx="19" cy="9" r="3" fill="none" stroke="#aaa" stroke-width="1.5"/><path d="M1 22c0-5 4-8 8-8s8 3 8 8M17 15c4 0 8 2 8 7" fill="none" stroke="#aaa" stroke-width="1.5"/></svg><span>Customized Solutions</span></div>
    <div class="benefit"><svg width="28" height="22" viewBox="0 0 28 22"><path d="M3 12l3-7h16l3 7v6H3z" fill="none" stroke="#aaa" stroke-width="1.5"/><circle cx="8" cy="18" r="2" fill="#aaa"/><circle cx="20" cy="18" r="2" fill="#aaa"/></svg><span>Vehicle Records</span></div>
  </div>
  <span class="btn more">See More</span>
</section>

<footer class="site-footer">
  <svg class="footer-pin" width="36" height="48" viewBox="0 0 36 48"><path d="M18 2C9 2 3 9 3 17c0 11 15 28 15 28s15-17 15-28C33 9 27 2 18 2z" fill="none" stroke="#fff" stroke-width="2"/><circle cx="18" cy="17" r="6" fill="none" stroke="#fff" stroke-width="2"/></svg>
  <p class="footer-brand">PermitSentry</p>
  <p class="footer-note">Driver license monitoring for companies and local government fleets, every day of the year.</p>
  <div class="contact-row">
    <div class="contact-card"><svg width="22" height="22" viewBox="0 0 24 24"><path d="M6 2l4 5-2 3c1 3 3 5 6 6l3-2 5 4-3 4C10 22 2 14 2 5z" fill="none" stroke="#fff" stroke-width="1.6"/></svg>0800-555-0142</div>
    <div class="contact-card"><svg width="22" height="22" viewBox="0 0 24 24"><rect x="6" y="1" width="12" height="22" rx="2" fill="none" stroke="#fff" stroke-width="1.6"/><line x1="10" y1="19" x2="14" y2="19" stroke="#fff" stroke-width="1.6"/></svg>0800-555-0142</div>
    <div class="contact-card"><svg width="24" height="20" viewBox="0 0 24 20"><path d="M1 9 23 1l-5 18-7-6z" fill="none" stroke="#fff" stroke-width="1.6"/><path d="M11 13l-2 6" stroke="#fff" stroke-width="1.6"/></svg>hello@permitsentry-demo.net</div>
  </div>
</footer>

<div class="bottom-bar">
  <span>PermitSentry © 2024. ALL RIGHTS RESERVED</span>
  <div class="social"><i></i><i></i><i></i><i></i></div>
</div>

</body>
</html>
```